500ml Aluminium drinking Water Bottle. Endlessly reusable and refillable

We need a label for our new 500ml water bottle. We are Corrie Vale Springs based in the Scottish Highlands. We extract filter and bottle drinking water from Loch Ness in Scotland. We currently have on the market a 100ml bottle of water designed for whisky drinkers see - www.fernhollowaqua.example
We now want to create a 500ml bottle of still and sparkling water using aluminium bottles which allows us much more room for branding. Our water will be exclusive and high end, not available in the supermarkets only selected outlets. Our current branding is based on the the number 126 which relates to the depth of the Loch at 126 Fathoms. We have interwound the legendary loch ness monster into the top half of the numbers. We will use the 126 logo on our new 500ml product but need a creative approach as to how it is presented on the bottle. Our 100ml Dew for Drams" product will stand alone, our new 500ml will use the same 126 logo, but its strap line will be changed to differentiate between our products. We need to maximise the available space on the aluminium bottle to ensure our product leaps out at the consumer. The available space for the new branding is 207mm wide x 120mm high, but in this space we need allow room for our barcode, address and statutory information, but we can scale these up or down. Our new design will be exclusive and elegant, not loud or harsh. It will represent a unique drinking water product from an iconic water source. So the branding of 126 is supplied. Our target consumer is middle aged and above with a disposable income,, those who want to experience rare and exclusive products and who are prepared to pay for that luxury.
Updates

Hi Guys - please fee free to use the 126 logo, but leave out "Dew for Drams". We are trying to create a label for 500ml aluminium bottles of still and sparkling drinking water for any occasion. We need the label design to be bold and vibrant but not brash or harsh. We are targeting exclusive retail and high end dining outlets, where the consumer will appreciate the pure water from the Scottish highlands. The history and scenery of Scotland should provide some inspiration for your designs or colour palette. We want to invoke thoughts of cold clear water and the refreshing taste of our pure water.

Target Market(s)

Exclusive high end consumers

Industry/Entity Type

food and drink

Requirements
Must have
• clear bright color scheme clever positioning of the logo
Should not have
• the term "Loch Ness Water" must not appear

```html
<!DOCTYPE html>
<html lang="en">
<head>
<meta charset="utf-8">
<title>Corrie Vale Springs – 500ml Aluminium Bottles</title>
<link rel="stylesheet" href="https://fonts.googleapis.com/css2?family=Open+Sans:wght@400;600&family=Great+Vibes&family=Montserrat:wght@700&display=swap">
<style>
  :root {
    --page: #ffffff;
    --alu-dark: #9d9c9f;
    --alu-mid: #c6c5c8;
    --alu-light: #fbfbfb;
    --outline: #111111;
    --rim: #3a3636;
    --thread: #a9a9ab;
    --label: #fdfdfd;
    --label-edge: #dcdcdc;
    --navy-blue: #1e5ea6;
    --sky-blue: #3aa6d6;
    --steel-blue: #4a7fb8;
    --drop-deep: #3b93d2;
    --drop-light: #72dcf4;
  }
  html, body {
    margin: 0;
    padding: 0;
    width: 942px;
    height: 1200px;
    overflow: hidden;
    background: var(--page);
  }
  .canvas {
    position: relative;
    width: 942px;
    height: 1200px;
  }
  .bottle {
    position: absolute;
    top: 0;
    width: 410px;
    height: 1200px;
  }
  .bottle--sparkling { left: 13px; }
  .bottle--still { left: 524px; }
  .bottle__art {
    position: absolute;
    inset: 0;
  }
  .bottle__text {
    position: absolute;
    left: 0;
    width: 410px;
    text-align: center;
    white-space: nowrap;
  }
  .brand-name {
    top: 575px;
    font-family: "Open Sans", sans-serif;
    font-weight: 600;
    font-size: 23px;
    letter-spacing: 0.5px;
    color: var(--navy-blue);
  }
  .origin-line {
    top: 803px;
    font-family: "Open Sans", sans-serif;
    font-weight: 400;
    font-size: 12.5px;
    letter-spacing: 1.6px;
    color: var(--navy-blue);
  }
  .water-type {
    top: 942px;
    font-family: "Open Sans", sans-serif;
    font-weight: 400;
    font-size: 12.5px;
    letter-spacing: 1.6px;
    color: var(--sky-blue);
  }
  .variant {
    top: 962px;
    font-family: "Great Vibes", cursive;
    font-size: 32px;
    color: var(--navy-blue);
  }
  .volume {
    top: 1014px;
    font-family: "Montserrat", sans-serif;
    font-weight: 700;
    font-size: 12.5px;
    color: var(--steel-blue);
  }
</style>
</head>
<body>
<main class="canvas">

  <!-- Sparkling variant -->
  <section class="bottle bottle--sparkling">
    <svg class="bottle__art" width="410" height="1200" viewBox="0 0 410 1200">
      <defs>
        <linearGradient id="aluSparkling" x1="0" x2="1" y1="0" y2="0">
          <stop offset="0" stop-color="var(--alu-mid)"/>
          <stop offset="0.42" stop-color="var(--alu-light)"/>
          <stop offset="0.6" stop-color="var(--alu-mid)"/>
          <stop offset="1" stop-color="var(--alu-dark)"/>
        </linearGradient>
        <linearGradient id="labelSparkling" x1="0" x2="1" y1="0" y2="0">
          <stop offset="0" stop-color="var(--label-edge)"/>
          <stop offset="0.18" stop-color="var(--label)"/>
          <stop offset="0.82" stop-color="var(--label)"/>
          <stop offset="1" stop-color="var(--label-edge)"/>
        </linearGradient>
        <linearGradient id="dropSparkling" x1="0" x2="1" y1="0" y2="0">
          <stop offset="0" stop-color="var(--drop-deep)"/>
          <stop offset="0.5" stop-color="var(--drop-light)"/>
          <stop offset="1" stop-color="var(--drop-deep)"/>
        </linearGradient>
      </defs>
      <path class="bottle-body" d="M92,12 L314,12 L314,127 C362,200 409,300 409,443 L409,1170 Q409,1189 390,1189 L20,1189 Q1,1189 1,1170 L1,443 C1,300 48,200 92,127 Z" fill="url(#aluSparkling)" stroke="var(--outline)" stroke-width="1.5"/>
      <rect class="bottle-rim" x="97" y="12" width="212" height="12" rx="6" fill="var(--rim)"/>
      <rect class="bottle-thread" x="89" y="62" width="228" height="8" rx="4" fill="var(--thread)"/>
      <rect class="bottle-thread" x="166" y="77" width="150" height="6" rx="3" fill="var(--thread)"/>
      <rect class="bottle-thread" x="86" y="97" width="234" height="13" rx="6" fill="var(--thread)"/>
      <rect class="label-band" x="1" y="766" width="408" height="285" fill="url(#labelSparkling)"/>
      <line x1="1" y1="1051" x2="409" y2="1051" stroke="#9a9a9a" stroke-width="1"/>
      <circle cx="210" cy="787" r="72" fill="var(--label)"/>
      <circle class="drop-art" role="img" aria-label="Blue water drop illustration with rising bubbles" cx="210" cy="787" r="64" fill="url(#dropSparkling)"/>
    </svg>
    <div class="bottle__text brand-name">Corrie Vale Springs</div>
    <div class="bottle__text origin-line">RESPECTFULLY EXTRACTED FROM LOCH NESS</div>
    <div class="bottle__text water-type">PURE NATURAL WATER</div>
    <div class="bottle__text variant">Sparkling</div>
    <div class="bottle__text volume">500ML</div>
  </section>

  <!-- Still variant -->
  <section class="bottle bottle--still">
    <svg class="bottle__art" width="410" height="1200" viewBox="0 0 410 1200">
      <defs>
        <linearGradient id="aluStill" x1="0" x2="1" y1="0" y2="0">
          <stop offset="0" stop-color="var(--alu-dark)"/>
          <stop offset="0.45" stop-color="var(--alu-light)"/>
          <stop offset="0.62" stop-color="var(--alu-mid)"/>
          <stop offset="1" stop-color="var(--alu-dark)"/>
        </linearGradient>
        <linearGradient id="labelStill" x1="0" x2="1" y1="0" y2="0">
          <stop offset="0" stop-color="var(--label-edge)"/>
          <stop offset="0.2" stop-color="var(--label)"/>
          <stop offset="0.8" stop-color="var(--label)"/>
          <stop offset="1" stop-color="var(--label-edge)"/>
        </linearGradient>
        <linearGradient id="dropStill" x1="0" x2="1" y1="0" y2="0">
          <stop offset="0" stop-color="var(--drop-deep)"/>
          <stop offset="0.5" stop-color="#7fcbeb"/>
          <stop offset="1" stop-color="#1fa3df"/>
        </linearGradient>
      </defs>
      <path class="bottle-body" d="M92,14 L314,14 L314,130 C362,203 409,303 409,446 L409,1172 Q409,1191 390,1191 L20,1191 Q1,1191 1,1172 L1,446 C1,303 48,203 92,130 Z" fill="url(#aluStill)" stroke="var(--outline)" stroke-width="1.5"/>
      <rect class="bottle-rim" x="97" y="14" width="212" height="12" rx="6" fill="var(--rim)"/>
      <rect class="bottle-thread" x="89" y="64" width="228" height="8" rx="4" fill="var(--thread)"/>
      <rect class="bottle-thread" x="166" y="79" width="150" height="6" rx="3" fill="var(--thread)"/>
      <rect class="bottle-thread" x="86" y="99" width="234" height="13" rx="6" fill="var(--thread)"/>
      <rect class="label-band" x="1" y="769" width="408" height="286" fill="url(#labelStill)"/>
      <line x1="1" y1="1055" x2="409" y2="1055" stroke="#9a9a9a" stroke-width="1"/>
      <circle cx="230" cy="790" r="72" fill="var(--label)"/>
      <circle class="drop-art" role="img" aria-label="Blue water drop illustration" cx="230" cy="790" r="64" fill="url(#dropStill)"/>
    </svg>
    <div class="bottle__text brand-name" style="top:578px; left:20px;">Corrie Vale Springs</div>
    <div class="bottle__text origin-line" style="top:806px; left:20px;">RESPECTFULLY EXTRACTED FROM LOCH NESS</div>
    <div class="bottle__text water-type" style="top:946px; left:20px;">PURE NATURAL WATER</div>
    <div class="bottle__text volume" style="top:1018px; left:20px;">500ML</div>
  </section>

</main>
</body>
</html>
```